Book Cover "Venice"

Creation of a cover (14 x 20.5 cm + bleed area) for a book:
Image: “BrumeVerte” (Tiff joined)
AUTHOR: Corinne Valmer
TITLE: The murmurs of Lorient
PUBLISHER: Editions Pluvane (AT THE BOTTOM OF THE COVER)

Target Market(s)

Readers of romantic novels

Industry/Entity Type

Book

```html
<!DOCTYPE html>
<html lang="fr">
<head>
<meta charset="utf-8">
<title>Les murmures de Lorient — Corinne Valmer</title>
<link rel="stylesheet" href="https://fonts.googleapis.com/css2?family=Young+Serif&display=swap">
<style>
  :root {
    --page-bg: #efedee;
    --cover-black: #000000;
    --copper-dark: #9a4c22;
    --copper-mid: #c98a55;
    --copper-light: #f6e1cc;
    --sky-red: #e8301c;
    --sky-orange: #f2541f;
    --sky-dusk: #7a2a2e;
    --night: #1a0c14;
    --pill-text: #140a06;
  }
  * { margin: 0; padding: 0; box-sizing: border-box; }
  html, body {
    width: 1200px; height: 1200px; overflow: hidden;
    background: var(--page-bg);
  }
  .cover {
    position: absolute; left: 233px; top: 70px;
    width: 734px; height: 1059px;
    background: var(--cover-black);
    overflow: hidden;
  }
  .cover-photo {
    position: absolute; left: 0; top: 0; width: 734px; height: 617px;
    background:
      linear-gradient(180deg, rgba(0,0,0,0) 45%, var(--night) 72%, var(--night) 100%),
      linear-gradient(180deg, var(--sky-dusk) 0%, var(--sky-orange) 22%, var(--sky-red) 45%, #b8261c 60%);
  }
  .copper-band {
    position: absolute; left: 0; top: 617px; width: 734px; height: 13px;
    background: linear-gradient(90deg, var(--copper-dark) 0%, var(--copper-mid) 35%, var(--copper-light) 50%, var(--copper-mid) 65%, var(--copper-dark) 100%);
  }
  .copper-text {
    background: linear-gradient(90deg, var(--copper-dark) 0%, var(--copper-mid) 30%, var(--copper-light) 50%, var(--copper-mid) 70%, var(--copper-dark) 100%);
    -webkit-background-clip: text; background-clip: text;
    color: transparent;
  }
  .title {
    position: absolute; left: 0; top: 648px; width: 734px;
    text-align: center;
    font-family: "Young Serif", Georgia, serif;
    font-weight: 400; font-size: 92px; line-height: 93px;
    letter-spacing: 0.5px;
  }
  .title span { display: block; }
  .author {
    position: absolute; left: 0; top: 940px; width: 734px;
    text-align: center;
    font-family: "Young Serif", Georgia, serif;
    font-size: 38px; line-height: 50px;
  }
  .publisher {
    position: absolute; left: 250px; top: 983px;
    width: 223px; height: 45px; border-radius: 13px;
    background: linear-gradient(90deg, var(--copper-dark) 0%, var(--copper-mid) 40%, var(--copper-light) 60%, var(--copper-mid) 80%, var(--copper-dark) 100%);
    color: var(--pill-text);
    font-family: "Young Serif", Georgia, serif;
    font-size: 24px; line-height: 45px; text-align: center;
  }
</style>
</head>
<body>
  <div class="cover">
    <div class="cover-photo" role="img" aria-label="Photographie : silhouettes de dômes d'église et de lampadaires allumés sous un ciel de coucher de soleil rouge flamboyant"></div>
    <div class="copper-band"></div>
    <h1 class="title copper-text"><span>Les murmures</span><span>de Lorient</span></h1>
    <p class="author copper-text">Corinne Valmer</p>
    <p class="publisher">Editions Pluvane</p>
  </div>
</body>
</html>
```